Heronby Mortgage Capital Business Card

We need a business card design for our mortgage servicing company. In addition to servicing the loans of homeowners, we help homeowners with purchasing their homes and any mortgage refinancing. We would like to see designs that use the colors in the logo attached below (gold-ish yellow and navy blue), and any other design you deem fit! The design should communicate a simpler life with smart mortgages provided by Heronby.

```html
<!DOCTYPE html>
<html lang="en">
<head>
<meta charset="utf-8">
<title>Heronby Mortgage Capital – Business Card</title>
<link href="https://fonts.googleapis.com/css2?family=Lato:wght@400;700&display=swap" rel="stylesheet">
<style>
  :root {
    --stage: #737373;
    --navy: #262050;
    --gold: #dfb13f;
    --ink: #262050;
  }
  * { margin: 0; padding: 0; box-sizing: border-box; }
  html, body {
    width: 1200px; height: 1000px; overflow: hidden;
    background: var(--stage);
    font-family: "Lato", sans-serif;
  }
  .card {
    position: absolute;
    width: 613px; height: 352px;
    box-shadow: 0 6px 18px rgba(0,0,0,0.25);
  }
  .card--front { left: 292px; top: 117px; background: var(--navy); }
  .card--back  { left: 294px; top: 542px; background: var(--gold); color: var(--ink); }

  .wordmark {
    position: absolute;
    font-family: "Lato", sans-serif;
    font-weight: 700;
    white-space: nowrap;
    display: flex; align-items: center;
  }
  .wordmark__dot { display: inline-block; border-radius: 50%; margin-right: 14px; }
  .card--front .wordmark {
    left: 0; right: 0; top: 160px; justify-content: center;
    font-size: 50px; color: var(--gold); letter-spacing: 0.5px;
  }
  .card--front .wordmark__dot { width: 18px; height: 18px; background: var(--gold); }
  .card--back .wordmark {
    left: 340px; top: 258px;
    font-size: 24px; color: var(--ink);
  }
  .card--back .wordmark__dot { width: 10px; height: 10px; background: var(--ink); margin-right: 8px; }

  .person { position: absolute; left: 64px; top: 86px; }
  .person__name { font-size: 23px; font-weight: 700; letter-spacing: 0.6px; line-height: 28px; }
  .person__role { font-size: 17px; letter-spacing: 0.6px; line-height: 20px; }

  .contact { position: absolute; left: 62px; top: 183px; font-size: 15px; letter-spacing: 0.9px; }
  .contact__row { display: flex; align-items: center; height: 19px; }
  .contact__icon { width: 14px; height: 12px; margin-right: 9px; fill: var(--ink); }

  .address { position: absolute; left: 62px; top: 244px; font-size: 15px; letter-spacing: 0.9px; line-height: 19px; font-style: normal; }
</style>
</head>
<body>
  <section class="card card--front" aria-label="Card front">
    <div class="wordmark"><span class="wordmark__dot"></span>Heronby Mortgage</div>
  </section>

  <section class="card card--back" aria-label="Card back">
    <div class="person">
      <div class="person__name">Name Surname</div>
      <div class="person__role">Position</div>
    </div>

    <div class="contact">
      <div class="contact__row">
        <svg class="contact__icon" viewBox="0 0 14 12" aria-hidden="true">
          <path d="M2.2 0.4 L4.3 0.2 L5.2 3 L3.9 4.1 C4.6 5.7 5.9 7 7.5 7.8 L8.7 6.6 L11.6 7.4 L11.5 9.6 C11.4 10.6 10.6 11.2 9.6 11 C5.2 10.2 1.6 6.7 0.9 2.3 C0.7 1.3 1.2 0.5 2.2 0.4 Z"/>
        </svg>
        <span>(888)-555-0142</span>
      </div>
      <div class="contact__row">
        <svg class="contact__icon" viewBox="0 0 14 12" aria-hidden="true">
          <path d="M0 1.5 H14 V10.5 H0 Z M0.8 2.2 L7 6.8 L13.2 2.2 V2 H0.8 Z" fill-rule="evenodd"/>
        </svg>
        <span>info@heronbymtg.com</span>
      </div>
    </div>

    <address class="address">
      218 Bayfront Ave S<br>
      Palm Harbor City<br>
      FL 33790
    </address>

    <div class="wordmark"><span class="wordmark__dot"></span>Heronby Mortgage</div>
  </section>
</body>
</html>
```